1200 x 150 pixel banner ad max size 200KB

Hi - I'm looking for an animated GIF to be used as an online digital banner advert.

The banner ad is to promote sales of gas cylinders from a world-leading manufacturer.

Headline 1: SLASH YOUR ADMINISTRATION COSTS BY 50%
Headline 2: If you're not happy with our service - we will give you your money back!
Headline 3 (if possible): FREE Regulator for all new customers/vessels

**The banner needs to really stand out of the page and reflect our company and brand - We exist to revolutionise ship safety, performance and crew welfare.**

The banner ad needs to include the product logo and company logo - both attached.

The blue colours in our logos are:
Dark Blue
Pantone 303
C100 M047 Y023 K079
R000 G031 B051
HTML 001F33

Light Blue
Pantone 2995
CO83 M001 Y000 K000
R080 G177 B234
HTML 05B1EA

Target Market(s)

Marine industry buyers - fleet managers, ship owners, technical purchasers, superintendants

Industry/Entity Type

Marine

Requirements
Must have
• Company colours, product and company logo

```html
<!DOCTYPE html>
<html lang="en">
<head>
<meta charset="utf-8">
<title>Money Back Guarantee Banner</title>
<link href="https://fonts.googleapis.com/css2?family=Roboto+Condensed:ital,wght@0,400;0,700;1,700&display=swap" rel="stylesheet">
<style>
  :root {
    --navy-deep: #001F33;
    --navy: #0a2440;
    --navy-mid: #123a63;
    --light-blue: #05B1EA;
    --sky: #3fb4ee;
    --gold: #f5b324;
    --gold-dark: #e08a0c;
    --white: #ffffff;
    --ink: #1b2230;
    --logo-blue: #0a4a8c;
  }
  * { margin: 0; padding: 0; box-sizing: border-box; }
  html, body { width: 1200px; height: 150px; overflow: hidden; background: var(--white); }
  .banner {
    position: relative;
    width: 1200px;
    height: 150px;
    overflow: hidden;
    font-family: "Roboto Condensed", "Arial Narrow", sans-serif;
    background: var(--white);
  }
  .banner__backdrop { position: absolute; inset: 0; }
  .cylinders {
    position: absolute; left: 0; top: 0; width: 150px; height: 150px;
    background: linear-gradient(90deg, #0b5fb8 0%, #2f8fe6 45%, #0b4f9c 100%);
    opacity: .9;
  }
  .person {
    position: absolute; left: 782px; top: 0; width: 218px; height: 150px;
    background: linear-gradient(180deg, #e9eef3 0%, #c9d4de 55%, #eef3f7 100%);
    clip-path: polygon(78px 0, 100% 0, 100% 100%, 18px 100%);
  }
  .seal {
    position: absolute; left: 168px; top: 14px; width: 112px; height: 112px;
    border-radius: 50%;
    background: radial-gradient(circle at 40% 35%, #ffe07a 0%, var(--gold) 45%, #c9820c 100%);
  }
  .headline {
    position: absolute; left: 305px; top: 14px;
    color: var(--white); font-weight: 700; text-transform: uppercase;
    line-height: 1;
  }
  .headline__line { display: block; font-size: 37px; letter-spacing: .3px; }
  .headline__line + .headline__line { margin-top: 4px; }
  .headline__gold { color: var(--gold); }
  .headline__blue { color: var(--light-blue); }
  .headline__sub {
    display: block; margin-top: 10px; font-size: 25px; font-style: italic;
  }
  .cta {
    position: absolute; z-index: 2; left: 662px; top: 56px; width: 164px; height: 42px;
    border-radius: 4px;
    background: linear-gradient(180deg, #ffd24a 0%, var(--gold) 50%, var(--gold-dark) 100%);
    box-shadow: 0 2px 4px rgba(0,0,0,.4);
    display: flex; align-items: center; justify-content: center; gap: 10px;
    color: var(--ink); font-weight: 700; font-size: 19px; text-transform: uppercase;
    text-decoration: none;
  }
  .cta__icon { width: 22px; height: 22px; flex: none; }
  .brand { position: absolute; white-space: nowrap; }
  .brand--company { top: 22px; left: 1020px; }
  .brand--product { top: 84px; left: 960px; display: flex; align-items: center; gap: 10px; }
  .brand__name {
    display: block; color: var(--logo-blue); font-weight: 700; font-size: 26px; line-height: 1;
  }
  .brand--product .brand__name { font-size: 30px; color: var(--navy-deep); }
  .brand__tag {
    display: block; color: var(--light-blue); font-size: 14px; font-weight: 400; margin-top: 6px; line-height: 1;
  }
  .brand--product .brand__tag { letter-spacing: 1.4px; font-weight: 700; font-size: 12px; margin-top: 5px; }
  .brand__mark {
    width: 44px; height: 44px; border-radius: 50%; background: var(--sky); flex: none;
  }
</style>
</head>
<body>
<div class="banner">
  <svg class="banner__backdrop" width="1200" height="150" viewBox="0 0 1200 150" aria-hidden="true">
    <defs>
      <linearGradient id="navyFill" x1="0" y1="0" x2="1" y2="0">
        <stop offset="0" stop-color="#0a2440"/>
        <stop offset=".6" stop-color="#0c2a4a"/>
        <stop offset="1" stop-color="#123a63"/>
      </linearGradient>
    </defs>
    <polygon points="0,0 842,0 782,150 0,150" fill="url(#navyFill)"/>
    <polygon points="842,0 860,0 800,150 782,150" fill="#05B1EA"/>
  </svg>

  <div class="cylinders" role="img" aria-label="Row of blue gas cylinders with regulators"></div>
  <div class="seal" role="img" aria-label="Gold 100% money back guarantee seal"></div>

  <h1 class="headline">
    <span class="headline__line">If you're <span class="headline__gold">not happy</span></span>
    <span class="headline__line">with <span class="headline__blue">our service...</span></span>
    <span class="headline__sub">We will give you your <span class="headline__gold">money back!</span></span>
  </h1>

  <div class="person" role="img" aria-label="Smiling engineer in a white hard hat and light blue shirt"></div>

  <a class="cta" href="#">
    Learn more
    <svg class="cta__icon" viewBox="0 0 22 22" aria-hidden="true">
      <circle cx="11" cy="11" r="11" fill="#ffffff"/>
      <path d="M9 6.5 L13.5 11 L9 15.5" fill="none" stroke="#1b2230" stroke-width="2.6" stroke-linecap="round" stroke-linejoin="round"/>
    </svg>
  </a>

  <div class="brand brand--company">
    <span class="brand__name">Norvale Marine</span>
    <span class="brand__tag">Innovative Ship Solutions</span>
  </div>

  <div class="brand brand--product">
    <span class="brand__mark" aria-hidden="true"></span>
    <div>
      <span class="brand__name">SwiftCylGas</span>
      <span class="brand__tag">QUALITY DELIVERED FAST</span>
    </div>
  </div>
</div>
</body>
</html>
```